Create website for home automation - Control your lighting, fans, blinds etc remotely by smartphone

Plan for SHOPIFY Website - Willowbyte Dwelling
Company name: Willowbyte Dwelling
Company Slogan: Calm Rooms Every Day
Clean, Modern, Easy to Navigate, easy to maintain - not a lot of coding. We need flash technology but displaying simply what we do.
What we provide:
We will be offering wireless switch which can be added to iOS/Android App via WiFi, allowing users to remotely turn on/off connected lights, fans, security cameras, appliances, irrigation, humidifier separately from anywhere at any time.
Control your home away from home. No more wandering of your mind on those lights or appliances which you might have left switched on. No need to drive back home to check and switch them off. Save that energy, money and time just with a click of your phone no matter how far you are from home.
Replace your home electrical switches with smart switches. They retrofit existing electrical switches and allow you to make the transformation as needed.
Easy to use and intuitive app allows you to control your lights and devices just at a click. Set any kind of ambiance suiting your occasion.
Set scenes in smartphone app to group and operate your devices just at a button click. Same device can be included in more than one scene.
Collections and Products
Light Switches
Wall Plugs
Fan Switch
Pendants etc special lighting types.
Light Dimmers
Blind Controllers
Home Page:
Home page needs to telling customers what we do and how we do it in a few words to grab people.
Logo
Phone
Email
Support – Download instructions per product
Client login
Wholesale login
Promotional video to be on home screen - this is a short 1.5 - 2 min illustration introduction video to who we are and what we do - this is yet to be created)
Social media link - Facebook
Pages:
FAQ
About Us
Support/Shipping/Returns policy
Support/Installation
Blog posts
Product pages:
Description
Price
Space for where a video will be featured - how each product works/installation.
Reviews
Our competition:
http://www.qorvat.com.au
https://brindlegadgetry.com.au/2018/04/05/best-smart-light-switches-and-plugs/
https://www.zelpinatech.com
Attachments:
Logo
Product pics
Promotional video - if ready

```html
<!DOCTYPE html>
<html lang="en">
<head>
<meta charset="utf-8">
<title>Willowbyte Dwelling – Login</title>
<link rel="stylesheet" href="https://fonts.googleapis.com/css2?family=Figtree:ital,wght@0,400;0,500;0,700;1,400&display=swap">
<style>
  :root {
    --brand-blue: #1076bf;
    --brand-navy: #0f3079;
    --ink: #444444;
    --white: #ffffff;
    --footer-bg: #282828;
    --social-blue: #1578c4;
  }
  * { box-sizing: border-box; margin: 0; padding: 0; }
  html, body { width: 960px; height: 1200px; overflow: hidden; background: var(--white); }
  body { font-family: "Figtree", Arial, sans-serif; color: var(--ink); position: relative; }

  .site-header { height: 92px; position: relative; background: var(--white); }
  .brand-small {
    position: absolute; left: 122px; top: 30px;
    display: flex; align-items: center; gap: 8px;
    color: var(--brand-navy); font-weight: 700; font-size: 15px; letter-spacing: 0.3px;
  }
  .brand-small .brand-mark { width: 18px; height: 18px; background: var(--brand-blue); }
  .main-nav {
    position: absolute; right: 112px; top: 37px;
    display: flex; gap: 26px; font-size: 12px;
  }
  .main-nav a { color: var(--ink); text-decoration: none; }

  .login-band {
    position: absolute; top: 92px; left: 0; width: 960px; height: 534px;
    background: var(--brand-blue); box-shadow: inset 0 2px 2px rgba(0,0,0,0.15);
  }
  .brand-large {
    position: absolute; top: 126px; left: 0; width: 100%;
    text-align: center; color: var(--white);
  }
  .brand-large .brand-mark {
    width: 64px; height: 64px; border-radius: 50%; background: var(--white);
    margin: 0 auto 22px;
  }
  .brand-large .brand-name { font-size: 27px; font-weight: 700; letter-spacing: 0.5px; line-height: 1; }
  .brand-large .brand-slogan { font-size: 11.5px; letter-spacing: 2.6px; margin-top: 4px; }

  .login-form { position: absolute; left: 359px; top: 258px; width: 242px; }
  .field {
    display: block; width: 242px; height: 41px; background: var(--white);
    border: none; padding: 0 15px; font: 400 11.5px "Figtree", Arial, sans-serif; color: var(--ink);
  }
  .field + .field { margin-top: 17px; }
  .sign-in {
    display: block; width: 242px; height: 28px; margin-top: 25px;
    background: var(--brand-navy); color: var(--white); border: none;
    font: 500 11.5px "Figtree", Arial, sans-serif;
  }
  .form-links { text-align: center; margin-top: 10px; font-size: 11.5px; }
  .form-links a { color: var(--white); display: block; }
  .forgot { font-style: italic; text-decoration: underline; }
  .sign-up { text-decoration: none; margin-top: 12px; }

  .site-footer {
    position: absolute; top: 626px; left: 0; width: 960px; height: 200px;
    background: var(--footer-bg); color: var(--white); text-align: center;
  }
  .footer-nav { display: flex; justify-content: center; gap: 27px; margin-top: 37px; font-size: 12px; }
  .footer-nav a { color: var(--white); text-decoration: none; }
  .social-links { display: flex; justify-content: center; gap: 6px; margin-top: 30px; }
  .social-links span { width: 19px; height: 19px; background: var(--social-blue); border-radius: 2px; }
  .company-details { margin-top: 18px; font-size: 11.5px; line-height: 14px; }
</style>
</head>
<body>
  <header class="site-header">
    <div class="brand-small"><span class="brand-mark"></span><span>WILLOWBYTE DWELLING</span></div>
    <nav class="main-nav">
      <a href="#">About Us</a><a href="#">Products</a><a href="#">Shipping</a>
      <a href="#">Support</a><a href="#">Blog</a><a href="#">Contact Us</a><a href="#">Login</a>
    </nav>
  </header>

  <main class="login-band">
    <div class="brand-large">
      <div class="brand-mark"></div>
      <div class="brand-name">WILLOWBYTE DWELLING</div>
      <div class="brand-slogan">Calm Rooms Every Day</div>
    </div>
    <form class="login-form">
      <input class="field" type="email" placeholder="Email Address">
      <input class="field" type="password" placeholder="Password">
      <button class="sign-in" type="button">Sign In</button>
      <div class="form-links">
        <a class="forgot" href="#">Forget Password ?</a>
        <a class="sign-up" href="#">Sign Up</a>
      </div>
    </form>
  </main>

  <footer class="site-footer">
    <nav class="footer-nav">
      <a href="#">Home</a><a href="#">About Us</a><a href="#">Products</a><a href="#">Shipping</a>
      <a href="#">Support</a><a href="#">Bog</a><a href="#">Contact Us</a><a href="#">Login</a>
    </nav>
    <div class="social-links" aria-label="Social links">
      <span></span><span></span><span></span><span></span><span></span><span></span><span></span>
    </div>
    <div class="company-details">
      <p>ABN: 47 215 903 668</p>
      <p>Office: 4/22 Fenwick Lane MARLOWE NSW 2090</p>
      <p>Telephone: (02) 5550 1847</p>
    </div>
  </footer>
</body>
</html>
```